Business Card Design Project - IT Company

CLOUD IT company working with medium to large corporate clients requires 2 sided Business Card design.

Strong, Professional and modern is what I am looking for.

The Logo JPG attached has all the colour palette options. which consist of Red and Silver on various backgrounds

Preferred option for the Back of card is either Silver Text on Red or Silver Text on Black. Though this is not concrete. Surprise me.

Logo must be prominent along with Contact details of the staff member

Tagline can be all Capitals " CLOUD MANAGED SERVICES"

I will look to provide feedback and tweaks to get the right design so it should be a fun process.

I will provide the layered files to the top few contenders.

Reason: Leaving the door open for some creativity. Don't forget this is an technology company. .

Target Market(s)

Leaders, decision makers, CEOs, CIOs,

Industry/Entity Type

Business

Requirements
Must have
• Data must have is

Company Name: Brelquist
Tagline: Cloud Managed Services

No Particular order

First Name Last name
Director
Mobile 0477 555 019
www.brelquist-example.com
First.Lastname@brelquist-example.com
Suite 7, 48 Wexmoor Lane, Sydney NSW 2000

```html
<!DOCTYPE html>
<html lang="en">
<head>
<meta charset="utf-8">
<title>Brelquist – Business Card</title>
<link rel="stylesheet" href="https://fonts.googleapis.com/css2?family=Open+Sans:wght@400;600;700;800&display=swap">
<style>
  :root {
    --stage: #e9e7e4;
    --red-deep: #7f161b;
    --red: #9b1f25;
    --red-text: #8c1a20;
    --silver: #d3d5d8;
    --silver-dim: #b9bcc0;
    --ink: #2b2b2d;
    --ink-soft: #4a4a4d;
    --paper: #fbfbfb;
    --rule: #bdbdbd;
    --ghost: #efe6e4;
  }
  * { box-sizing: border-box; margin: 0; padding: 0; }
  html, body { width: 1200px; height: 880px; overflow: hidden; }
  body {
    background: var(--stage);
    font-family: "Open Sans", Arial, sans-serif;
    display: flex;
    align-items: center;
    justify-content: center;
    gap: 40px;
  }
  .card {
    position: relative;
    width: 540px;
    height: 309px;
    border-radius: 4px;
    overflow: hidden;
    box-shadow: 0 10px 28px rgba(0,0,0,.18);
  }

  /* Front: red side */
  .card-front {
    background: linear-gradient(160deg, var(--red) 0%, var(--red-deep) 100%);
    color: var(--silver);
  }
  .front-brand {
    position: absolute;
    left: 0; right: 0; top: 78px;
    display: flex;
    align-items: center;
    justify-content: center;
    gap: 18px;
  }
  .front-brand .brand-dot {
    width: 56px; height: 56px;
    border-radius: 50%;
    background: var(--silver);
  }
  .front-brand .brand-name {
    font-size: 64px;
    font-weight: 700;
    line-height: 1;
    color: var(--silver);
  }
  .front-tagline {
    position: absolute;
    left: 0; right: 0; top: 164px;
    text-align: center;
    font-size: 15px;
    font-weight: 700;
    letter-spacing: .5px;
    color: var(--silver);
  }
  .front-rule {
    position: absolute;
    left: 100px; right: 100px; top: 218px;
    height: 2px;
    background: linear-gradient(90deg, transparent, var(--silver-dim), transparent);
  }
  .front-web {
    position: absolute;
    left: 0; right: 0; top: 236px;
    text-align: center;
    font-size: 15px;
    letter-spacing: 2.5px;
    color: var(--silver);
  }
  .front-web strong { font-weight: 700; }

  /* Back: white side */
  .card-back {
    background: var(--paper);
    color: var(--ink);
  }
  .back-brand {
    position: absolute;
    left: 26px; top: 24px;
  }
  .back-brand .brand-row {
    display: flex;
    align-items: center;
    gap: 8px;
  }
  .back-brand .brand-dot {
    width: 24px; height: 24px;
    border-radius: 50%;
    background: var(--red);
  }
  .back-brand .brand-name {
    font-size: 28px;
    font-weight: 700;
    line-height: 1;
    color: var(--ink);
  }
  .back-brand .brand-tagline {
    margin-left: 32px;
    font-size: 8.5px;
    font-weight: 700;
    color: var(--ink);
    letter-spacing: .2px;
  }
  .back-ghost {
    position: absolute;
    left: 40px; top: 96px;
    width: 170px; height: 170px;
    border-radius: 50%;
    border: 22px solid var(--ghost);
  }
  .back-details {
    position: absolute;
    right: 30px; top: 96px;
    width: 250px;
    text-align: right;
  }
  .person-name {
    font-size: 24px;
    font-weight: 800;
    color: var(--red-text);
    line-height: 1.1;
  }
  .person-role {
    font-size: 11px;
    color: var(--ink-soft);
    margin-top: 2px;
  }
  .detail-rule {
    height: 1px;
    background: var(--rule);
    margin: 9px 0;
  }
  .contact-list { list-style: none; }
  .contact-list li {
    display: flex;
    justify-content: flex-end;
    align-items: center;
    gap: 7px;
    font-size: 11px;
    line-height: 1.75;
    color: var(--ink);
  }
  .contact-list .icon { width: 11px; height: 11px; flex: none; }
  .contact-list .no-icon { width: 11px; flex: none; }
  .address {
    display: flex;
    justify-content: flex-end;
    align-items: flex-end;
    gap: 7px;
    font-size: 11px;
    line-height: 1.6;
  }
  .address .icon { width: 11px; height: 14px; flex: none; margin-bottom: 3px; }
</style>
</head>
<body>

  <section class="card card-front" aria-label="Card front">
    <div class="front-brand">
      <span class="brand-dot"></span>
      <span class="brand-name">Brelquist</span>
    </div>
    <p class="front-tagline">CLOUD MANAGED SERVICES</p>
    <div class="front-rule"></div>
    <p class="front-web">www.<strong>brelquist-example</strong>.com</p>
  </section>

  <section class="card card-back" aria-label="Card back">
    <div class="back-brand">
      <div class="brand-row">
        <span class="brand-dot"></span>
        <span class="brand-name">Brelquist</span>
      </div>
      <p class="brand-tagline">CLOUD MANAGED SERVICES</p>
    </div>

    <div class="back-ghost"></div>

    <div class="back-details">
      <h1 class="person-name">Dorian Kessler</h1>
      <p class="person-role">Director</p>
      <div class="detail-rule"></div>
      <ul class="contact-list">
        <li>dorian.kessler@brelquist-example.com<span class="no-icon"></span></li>
        <li>0477 555 019
          <svg class="icon" viewBox="0 0 12 12" aria-hidden="true"><rect x="3" y="0.5" width="6" height="11" rx="1.2" fill="#9b1f25"/><rect x="4" y="2" width="4" height="6" fill="#fbfbfb"/></svg>
        </li>
        <li>www.brelquist-example.com
          <svg class="icon" viewBox="0 0 12 12" aria-hidden="true"><rect x="0.5" y="2" width="11" height="8" rx="1" fill="#9b1f25"/><path d="M1 2.8 6 6.6 11 2.8" fill="none" stroke="#fbfbfb" stroke-width="1"/></svg>
        </li>
      </ul>
      <div class="detail-rule"></div>
      <div class="address">
        <p>Suite 7, Level 2<br>48 Wexmoor Lane<br>SYDNEY NSW 2000</p>
        <svg class="icon" viewBox="0 0 12 16" aria-hidden="true"><path d="M6 0.5a5 5 0 0 1 5 5c0 3.6-5 10-5 10s-5-6.4-5-10a5 5 0 0 1 5-5z" fill="#9b1f25"/><circle cx="6" cy="5.5" r="1.8" fill="#fbfbfb"/></svg>
      </div>
    </div>
  </section>

</body>
</html>
```